VRUM Diagnostics App - zOS

I need some UI artwork (2D) for my already released zOS app: "VRUM Kv" I'd like the UI to look more like an in-dash head-unit in a car. I'm in the process of updating the app with Tabro support and would like to release this next version with a brand new UI.

A lot of car audio enthusiast already use my app and probably mount their Pellix/Pello near their car audio components on the dash. Most of the car audio deck Mfgs support a few colors: Green/Blue/Amber/Red I'd like to offer these themes as well. But I will settle for the Amber color to match my existing App icon scheme. (nice to have)

My UI is incredibly simple. It's just a bunch of up/down buttons. I plan to do some animations an will need some room blocked off for this to the left of LCD text.

Screenshots are of my existing zOS app for Pellix and the half assed job I did for Tabro. - Note: These are the only two orientations I plan to use. But the resolution in these photos are smaller than my requirements. See "Must Haves" for all four resolutions.

update: I'd like something to imitate the style of the skin in the following: http://quorvel.artmosaicnet.example/art/Plomtune-KXP14-Skin-71824069

Thanks!

Target Market(s)

Car Audio Enthusiasts

Industry/Entity Type

Audio

Requirements
Must have
• - Static background that looks like an in-dash stereo. (think plomtune skin)
- An LCD area where I can display some text and stats on left (see Tabro ss)
- UI buttons that support up/down states. When the user presses a button, it stays "down" until it's tapped again or another is pushed.
- UI toggle switch for Wobble mode (see ss)

Pellix/Pello resolutions
-
- Landscape for Pellix4/4T Clarion (960 x 640)
- Landscape for Pellix 5 Clarion (1136 x 640)

Tabro resolutions
-
- This UI has more buttons and taller, but I'd like a similar look and feel
- Landscape for Tabro Clarion (2048 x 1536)
- Landscape for Tabro2/lite (1024 x 768)

Other Controls:
- An empty space for UI slider control. I will place this over artwork. (see ss)
- Emergency stop button should be red and easily accessible. Slightly larger than other buttons.

Pellix Buttons/Controls
-
20,30,40,50,60,70,80,90,100,150,250,300
Toggle Switch, P button, S button, Stop button

Tabro Buttons/Controls
-
20,25,30,35,40,45,50,55,60,65,70,80,90,110,125,150,250,300
Instant VRUM Buttons: 20,25,30,35,40,45,50,55

Disregard the waveform animation in the screenshots (squiggly line at bottom) I plan do a small animation to the left of the text in the LCD area.
Nice to have
• - Theme for LED-like colors: Green/Blue/Amber/Red on-off buttons
Should not have
• - sharp corners on buttons
- stretched version of Pellix layout for the Tabro.

```html
<!DOCTYPE html>
<html lang="en">
<head>
<meta charset="utf-8">
<title>VRUM Kv — Tone Generator</title>
<link rel="stylesheet" href="https://fonts.googleapis.com/css2?family=Orbitron:wght@500;700&family=Roboto:wght@700;900&display=swap">
<style>
  :root {
    --bg-top: #1c1c1c;
    --bg-bottom: #2e2e2e;
    --bar-black: #000000;
    --white: #ffffff;
    --lcd-red: #ff1a0a;
    --lcd-line: rgba(120, 0, 0, 0.45);
    --frame: #6a6a6a;
    --frame-dark: #3a3a3a;
    --key-top: #ff8a78;
    --key-mid: #ff6a1a;
    --key-low: #ff2400;
    --key-down-top: #a01000;
    --key-down-low: #d01800;
    --ink: #0a0a0a;
    --steel-light: #f4f4f4;
    --steel-dark: #a8a8a8;
  }
  * { box-sizing: border-box; margin: 0; padding: 0; }
  html, body { width: 1200px; height: 800px; overflow: hidden; }
  body {
    position: relative;
    background: linear-gradient(180deg, var(--bg-top) 0%, var(--bg-bottom) 100%);
    font-family: "Roboto", Arial, sans-serif;
    color: var(--white);
  }

  /* status bar */
  .status-bar {
    position: absolute; left: 0; top: 0; width: 1200px; height: 52px;
    background: var(--bar-black);
    font-weight: 700; font-size: 30px;
  }
  .status-bar .signal { position: absolute; left: 18px; top: 14px; }
  .status-bar .carrier { position: absolute; left: 70px; top: 8px; }
  .status-bar .wifi { position: absolute; left: 165px; top: 10px; }
  .status-bar .clock { position: absolute; left: 0; width: 1200px; top: 8px; text-align: center; }
  .status-bar .battery { position: absolute; right: 16px; top: 12px; }

  /* LCD readout */
  .lcd {
    position: absolute; left: 60px; top: 107px; width: 1064px; height: 112px;
    border-radius: 20px;
    border: 3px solid var(--frame);
    box-shadow: 0 4px 0 var(--frame-dark), inset 0 0 12px rgba(0,0,0,0.35);
    background:
      repeating-linear-gradient(90deg, transparent 0 24px, var(--lcd-line) 24px 25px),
      repeating-linear-gradient(180deg, transparent 0 16px, var(--lcd-line) 16px 17px),
      var(--lcd-red);
    text-align: center;
  }
  .lcd-value {
    position: absolute; left: 0; width: 100%; top: 10px;
    font-family: "Orbitron", "Courier New", monospace; font-weight: 700;
    color: var(--ink); font-size: 82px; letter-spacing: 2px;
    font-style: italic;
  }
  .lcd-value .unit { font-size: 36px; letter-spacing: 0; margin-left: 2px; }

  /* frequency keypad */
  .keypad {
    position: absolute; left: 58px; top: 242px; width: 1071px; height: 246px;
    border-radius: 12px; border: 3px solid var(--frame);
    box-shadow: 0 4px 0 var(--frame-dark);
    background: var(--frame-dark);
    display: grid; grid-template-columns: repeat(6, 1fr); grid-template-rows: repeat(2, 1fr);
    gap: 2px; overflow: hidden;
  }
  .key {
    background: linear-gradient(180deg, var(--key-top) 0%, var(--key-mid) 45%, var(--key-low) 55%, var(--key-low) 100%);
    display: flex; align-items: center; justify-content: center;
    font-family: "Orbitron", "Courier New", monospace; font-weight: 500;
    font-size: 58px; color: var(--ink); font-style: italic;
    -webkit-text-stroke: 1px var(--white);
  }
  .key.is-down {
    background: linear-gradient(180deg, var(--key-down-top) 0%, var(--key-down-top) 50%, var(--key-down-low) 55%, var(--key-down-low) 100%);
  }

  /* slider */
  .slider-track {
    position: absolute; left: 58px; top: 518px; width: 1074px; height: 38px;
    border-radius: 19px; border: 3px solid var(--frame);
    background: linear-gradient(180deg, var(--key-top) 0%, var(--key-mid) 40%, var(--key-low) 60%);
    box-shadow: 0 3px 0 var(--frame-dark);
  }
  .knob {
    position: absolute; border-radius: 50%;
    background: radial-gradient(circle at 50% 40%, var(--steel-light) 0%, var(--steel-dark) 100%);
    border: 2px solid #888;
    box-shadow: 0 2px 5px rgba(0,0,0,0.6);
  }
  .slider-knob { left: 476px; top: 506px; width: 62px; height: 62px; }

  /* wobble toggle */
  .wobble-label { position: absolute; left: 66px; top: 596px; font-size: 28px; font-weight: 700; }
  .toggle {
    position: absolute; left: 63px; top: 637px; width: 166px; height: 62px;
    border-radius: 31px; border: 3px solid var(--frame);
    background: linear-gradient(180deg, var(--key-top) 0%, var(--key-mid) 40%, var(--key-low) 60%);
    box-shadow: 0 3px 0 var(--frame-dark);
  }
  .toggle-knob { left: 65px; top: 640px; width: 58px; height: 58px; }
  .toggle-state {
    position: absolute; left: 138px; top: 649px; font-size: 28px; font-weight: 900; color: var(--ink);
  }

  /* mode controls */
  .mode-label { position: absolute; top: 596px; font-size: 28px; font-weight: 700; text-align: center; }
  .mode-label.pink { left: 468px; width: 230px; }
  .mode-label.sweep { left: 730px; width: 190px; }
  .mode-bar { position: absolute; left: 438px; top: 580px; }
  .mode-key { position: absolute; top: 648px; font-size: 36px; font-weight: 900; color: var(--ink); }
  .mode-key.p { left: 551px; }
  .mode-key.s { left: 798px; }
  .stop-label { position: absolute; left: 976px; top: 620px; font-size: 40px; font-weight: 900; color: var(--ink); }
</style>
</head>
<body>
  <header class="status-bar">
    <svg class="signal" width="38" height="22" viewBox="0 0 38 22" aria-hidden="true">
      <rect x="0" y="14" width="6" height="8" fill="#fff"/>
      <rect x="9" y="10" width="6" height="12" fill="#fff"/>
      <rect x="18" y="5" width="6" height="17" fill="#fff"/>
      <rect x="27" y="0" width="6" height="22" fill="#fff"/>
    </svg>
    <span class="carrier">Kestrel</span>
    <svg class="wifi" width="36" height="28" viewBox="0 0 36 28" aria-hidden="true">
      <path d="M2 10 A22 22 0 0 1 34 10" stroke="#fff" stroke-width="4" fill="none"/>
      <path d="M8 16 A14 14 0 0 1 28 16" stroke="#fff" stroke-width="4" fill="none"/>
      <path d="M14 22 L18 27 L22 22 A6 6 0 0 0 14 22 Z" fill="#fff"/>
    </svg>
    <span class="clock">12:34 PM</span>
    <svg class="battery" width="48" height="26" viewBox="0 0 48 26" aria-hidden="true">
      <rect x="1.5" y="1.5" width="40" height="23" rx="3" stroke="#fff" stroke-width="3" fill="none"/>
      <rect x="5" y="5" width="33" height="16" fill="#fff"/>
      <rect x="43" y="8" width="4" height="10" fill="#fff"/>
    </svg>
  </header>

  <section class="lcd">
    <div class="lcd-value">32.7<span class="unit">HZ</span></div>
  </section>

  <section class="keypad">
    <div class="key is-down">20</div>
    <div class="key">30</div>
    <div class="key">40</div>
    <div class="key">50</div>
    <div class="key">60</div>
    <div class="key">70</div>
    <div class="key">80</div>
    <div class="key">90</div>
    <div class="key">100</div>
    <div class="key">150</div>
    <div class="key">250</div>
    <div class="key">300</div>
  </section>

  <div class="slider-track"></div>
  <div class="knob slider-knob"></div>

  <div class="wobble-label">+10 Hz Wobble</div>
  <div class="toggle"></div>
  <div class="knob toggle-knob"></div>
  <div class="toggle-state">OFF</div>

  <div class="mode-label pink">Pink Noise</div>
  <div class="mode-label sweep">Sweep</div>
  <svg class="mode-bar" width="692" height="124" viewBox="0 0 692 124" aria-hidden="true">
    <defs>
      <linearGradient id="bar-fill" x1="0" y1="0" x2="0" y2="1">
        <stop offset="0" stop-color="#ff8a78"/>
        <stop offset="0.4" stop-color="#ff6a1a"/>
        <stop offset="0.6" stop-color="#ff2400"/>
      </linearGradient>
      <linearGradient id="stop-fill" x1="0" y1="0" x2="0" y2="1">
        <stop offset="0" stop-color="#f6f6f6"/>
        <stop offset="1" stop-color="#a4a4a4"/>
      </linearGradient>
    </defs>
    <path d="M32 57 H520 V119 H32 A31 31 0 0 1 32 57 Z" fill="url(#bar-fill)" stroke="#6a6a6a" stroke-width="3"/>
    <line x1="270" y1="60" x2="240" y2="116" stroke="#cc1000" stroke-width="2"/>
    <path d="M548 4 H666 A22 22 0 0 1 688 26 V96 A22 22 0 0 1 666 118 H484 Z" fill="url(#stop-fill)" stroke="#7a7a7a" stroke-width="3"/>
  </svg>
  <div class="mode-key p">P</div>
  <div class="mode-key s">S</div>
  <div class="stop-label">STOP</div>
</body>
</html>
```